Website for Verdix Partners

We need to create a website for our company. Attached is the site map of the website and data input needed. Our theme colour is RED and our Logo is attached

We need a very attractive design where graphics are largely used like flash.

The main idea of the website is to show Telecommunications Suppliers World Wide that we could assist them in getting more business in Africa and Middle East through our local presence in this region.

Target Market(s)

Telecommunication Suppliers and Clients

Industry/Entity Type

Business

Font styles to use
Serif
Sans Serif

Colors
ec2027

Requirements
Must have
• Graphics that shows Telecommunications Suppliers World Wide that we could assist them in getting more business in Africa and Middle East through our local presence in this region.

The website should be easy to edit for future changes by us.
Nice to have
• New ideas

```html
<!DOCTYPE html>
<html lang="en">
<head>
<meta charset="utf-8">
<title>Verdix Partners</title>
<link href="https://fonts.googleapis.com/css2?family=Open+Sans:wght@300;400;600;700&display=swap" rel="stylesheet">
<style>
:root{
  --red:#ec2027;
  --ink:#333;
  --muted:#666;
  --panel:#f2f2f2;
  --slate:#5d5d5f;
  --footer:#5a5a5b;
  --base:#3e3e3f;
  --white:#fff;
}
*{box-sizing:border-box;margin:0;padding:0}
html,body{width:726px;height:1200px;overflow:hidden;background:var(--white);font-family:"Open Sans",Arial,sans-serif;color:var(--ink)}
.page{position:relative;width:726px;height:1200px}
.abs{position:absolute}
.topbar{top:0;left:0;width:726px;height:28px;display:flex;justify-content:flex-end;align-items:center;gap:14px;padding-right:45px;font-size:8.3px;color:var(--red)}
.topbar span{display:flex;align-items:center;gap:5px}
.header{top:28px;left:0;width:726px;height:54px;background:#f7f7f7;border-top:1px solid #e6e6e6}
.brand{left:44px;top:17px;display:flex;align-items:center;gap:7px;font-size:16px;font-weight:600;color:var(--ink);letter-spacing:.5px}
.brand i{width:15px;height:15px;background:var(--red);display:block}
.nav{right:34px;top:0;height:54px;display:flex;font-size:7.5px;text-transform:uppercase}
.nav a{display:flex;align-items:center;padding:0 10.5px;color:var(--ink);text-decoration:none;height:54px}
.nav a.on{color:var(--red);border-bottom:2px solid var(--red);height:37px;margin-top:17px;align-items:flex-start;padding-top:6px}
.hero{top:82px;left:0;width:726px;height:288px;overflow:hidden;
  background:
   radial-gradient(ellipse 120px 150px at 545px 150px,rgba(236,200,180,.95),rgba(214,170,150,.6) 55%,transparent 80%),
   radial-gradient(ellipse 140px 120px at 545px 60px,rgba(120,85,60,.55),transparent 70%),
   radial-gradient(ellipse 90px 110px at 300px 90px,rgba(170,140,120,.45),transparent 75%),
   linear-gradient(90deg,#4d4b49 0%,#6a6561 35%,#8d7f76 60%,#6e625b 85%,#403c3a 100%)}
.hero h1{position:absolute;left:46px;top:94px;color:var(--white);font-size:31px;font-weight:600;line-height:32px;letter-spacing:.5px;text-shadow:0 1px 2px rgba(0,0,0,.3)}
.hero h1 em{font-style:normal;color:var(--red)}
.dots{left:45px;top:337px;display:flex;gap:4px}
.dots b{width:9px;height:9px;border-radius:50%;background:var(--white)}
.dots b:first-child{background:var(--red)}
.card{top:393px;width:200px;height:242px;background:var(--panel);text-align:center}
.card h2{font-size:15px;font-weight:400;color:var(--red);margin-top:15px}
.card .photo{width:175px;height:89px;margin:9px auto 0}
.card p{font-size:8px;line-height:12.8px;color:var(--muted);padding:0 11px;margin-top:10px}
.btn{display:inline-block;background:var(--red);color:var(--white);font-size:7.5px;font-weight:600;border-radius:12px;padding:5px 14px;text-transform:uppercase}
.card .btn{position:absolute;left:63px;bottom:-11px;padding:6px 13px}
.box{left:480px;width:201px;background:var(--slate);color:var(--white);padding:10px 14px}
.box h3{font-size:15px;font-weight:300;line-height:17px;text-transform:uppercase}
.box p{font-size:7.8px;line-height:12.3px;margin-top:8px;font-weight:400}
.box .more{font-size:6.5px;font-weight:600;text-align:right;margin-top:6px}
.rule{top:668px;left:44px;width:637px;height:1px;background:#ddd}
.port-title{top:684px;left:0;width:726px;text-align:center;font-size:16px;color:var(--red);font-weight:400}
.port-text{top:709px;left:90px;width:546px;text-align:center;font-size:7.8px;line-height:12.8px;color:var(--muted)}
.tile{width:200px;height:115px;overflow:hidden}
.tile span{position:absolute;left:0;bottom:0;width:100%;height:25px;background:rgba(30,30,30,.75);color:var(--white);font-size:8.5px;font-weight:600;padding:7px 11px}
.footer{top:1009px;left:0;width:726px;height:150px;background:var(--footer);color:var(--white)}
.footer h4{font-size:13px;font-weight:300;text-transform:uppercase}
.footer p{font-size:7.8px;line-height:12.8px;color:#ddd}
.divider{left:371px;top:22px;width:1px;height:112px;background:#777}
.base{top:1159px;left:0;width:726px;height:41px;background:var(--base);color:#bbb;font-size:6.5px;text-align:center;line-height:41px}
.social{display:flex;gap:6px}
.social b{width:18px;height:18px;border-radius:50%}
</style>
</head>
<body>
<div class="page">
  <div class="abs topbar">
    <span><svg width="8" height="9" viewBox="0 0 8 9"><rect width="8" height="9" rx="1.5" fill="#555"/><rect x="2" y="1.5" width="4" height="6" fill="#fff"/></svg>121 555 0148</span>
    <span><svg width="10" height="7" viewBox="0 0 10 7"><rect width="10" height="7" fill="#555"/><path d="M0 0 L5 4 L10 0" stroke="#fff" fill="none"/></svg>info@verdix-partners.com</span>
  </div>
  <header class="abs header">
    <div class="abs brand"><i></i>VERDIX PARTNERS</div>
    <nav class="abs nav">
      <a class="on">Home</a><a>Company</a><a>Portfolio</a><a>Footprint</a><a>Location</a><a>Contact Us</a>
    </nav>
  </header>
  <section class="abs hero" role="img" aria-label="Smiling support agent wearing a headset, with a blurred colleague behind">
    <h1>YOUR <em>CHALLENGE</em> IS<br>OUR BUSINESS</h1>
  </section>
  <div class="abs dots"><b></b><b></b><b></b><b></b></div>

  <article class="abs card" style="left:44px">
    <h2>WHO WE ARE</h2>
    <div class="photo" role="img" aria-label="Business team in an office" style="background:radial-gradient(ellipse 30px 45px at 40px 40px,#e8d2c4,transparent 80%),radial-gradient(ellipse 35px 45px at 140px 55px,#dcc0ae,transparent 80%),linear-gradient(90deg,#f3f3f3,#2e3138 35%,#e9eaec 55%,#30343c 80%,#f0f0f0)"></div>
    <p>Verdix Partners is a leading telecommunication Solution Provider; the company provides state of the art technologies and turnkey solutions to its clients that fully support their business needs from planning right through full operation..</p>
    <span class="btn">Read More</span>
  </article>
  <article class="abs card" style="left:262px">
    <h2>WHAT WE DO</h2>
    <div class="photo" role="img" aria-label="Call centre staff with headsets" style="background:radial-gradient(ellipse 40px 45px at 135px 50px,#f1dcc8,#e8cfa0 50%,transparent 85%),radial-gradient(ellipse 40px 35px at 60px 30px,#d9c7b8,transparent 80%),linear-gradient(135deg,#f2f3f5,#c9d1db 60%,#8c98a6)"></div>
    <p>Verdix Partners is a leading telecommunication Solution Provider; the company provides state of the art technologies and turnkey solutions to its clients that fully support their business needs from planning right through full operation..</p>
    <span class="btn">Read More</span>
  </article>
  <div class="abs box" style="top:393px;height:109px">
    <h3>Our<br>Mission</h3>
    <p>Becoming the service partner of choice for Communication &amp; Information technology services.</p>
    <div class="more">READ MORE &gt;&gt;</div>
  </div>
  <div class="abs box" style="top:514px;height:121px">
    <h3>Our<br>Vision</h3>
    <p>Leveraging telecommunications edge by providing world class support and services that empower people to connect and businesses to grow.</p>
    <div class="more">READ MORE &gt;&gt;</div>
  </div>

  <div class="abs rule"></div>
  <h2 class="abs port-title">OUR PORTFOLIO</h2>
  <p class="abs port-text">Aliquam molestie, mi et imperdiet euismod, dui purus auctor tellus, et interdum lacus lectus et ante. Sed accumsan sollicitudin sapien, sit amet adipiscing turpis gravida ac. In congue, neque ac lobortis volutpat, libero mauris varius mi, vitae suscipit ipsum ligula vitae risus.</p>

  <div class="abs tile" style="left:44px;top:750px;background:radial-gradient(ellipse 35px 25px at 95px 30px,#e4343b,transparent 80%),radial-gradient(ellipse 70px 40px at 45px 55px,#2e7fc9,transparent 85%),linear-gradient(180deg,#5a5e66,#d7d9dc 45%,#f2f2f2)" role="img" aria-label="Network cables plugged into a switch"><span>Access Network Solutions</span></div>
  <div class="abs tile" style="left:262px;top:750px;background:radial-gradient(ellipse 90px 55px at 100px 80px,#5d8fc4,transparent 80%),radial-gradient(ellipse 60px 30px at 60px 20px,#2a4d7a,transparent 80%),linear-gradient(135deg,#0b1c33,#1d3c62 60%,#0d1d35)" role="img" aria-label="Glowing globe with connection lines"><span>Transmission Network Solutions</span></div>
  <div class="abs tile" style="left:481px;top:750px;background:radial-gradient(ellipse 40px 18px at 30px 15px,rgba(240,150,40,.5),transparent 80%),radial-gradient(ellipse 40px 18px at 170px 30px,rgba(236,32,39,.35),transparent 80%),radial-gradient(ellipse 40px 20px at 175px 75px,rgba(150,200,60,.35),transparent 80%),radial-gradient(ellipse 35px 45px at 120px 40px,#55524f,transparent 80%),linear-gradient(135deg,#232323,#3a3a3a)" role="img" aria-label="Chalkboard diagram of business behaviours"><span>Core Network Solutions</span></div>
  <div class="abs tile" style="left:44px;top:877px;background:radial-gradient(ellipse 25px 15px at 80px 20px,#e6c3a8,transparent 80%),linear-gradient(180deg,transparent 70%,#4e9a30 85%),linear-gradient(90deg,#f6f6f6 45%,#6fb2e6 60%,#2f7fc4 100%)" role="img" aria-label="Hand placing a cube into a sky and grass block wall"><span>Value Added Services</span></div>
  <div class="abs tile" style="left:262px;top:877px;background:radial-gradient(ellipse 50px 50px at 60px 45px,rgba(255,255,255,.6),transparent 80%),linear-gradient(90deg,#c9ccd0 0%,#9a9da2 50%,#2b2b2d 70%,#1c1c1d)" role="img" aria-label="Businessman touching a virtual screen"><span>Managed Services</span></div>
  <div class="abs tile" style="left:481px;top:877px;background:radial-gradient(ellipse 30px 25px at 130px 30px,#6a4a38,transparent 80%),radial-gradient(ellipse 50px 35px at 50px 60px,#2c3850,transparent 80%),linear-gradient(180deg,#c5d7e6,#7d97b2 50%,#3a4658)" role="img" aria-label="Business meeting around a table"><span>Business Consultancy</span></div>

  <footer class="abs footer">
    <h4 class="abs" style="left:44px;top:18px">Career With Us</h4>
    <div class="abs" role="img" aria-label="Team of office workers" style="left:44px;top:44px;width:93px;height:73px;background:radial-gradient(ellipse 12px 14px at 18px 18px,#e2c7b4,transparent 85%),radial-gradient(ellipse 12px 14px at 48px 22px,#e6cdb9,transparent 85%),radial-gradient(ellipse 12px 14px at 78px 18px,#dcc1ad,transparent 85%),linear-gradient(180deg,#eef0f2 30%,#2d3038 60%,#b8bcc2)"></div>
    <p class="abs" style="left:147px;top:42px;width:210px">Aliquam molestie, mi et imperdiet euismod, dui purus auctor tellus, et interdum lacus lectus et ante. Sed accumsan sollicitudin sapien, sit amet adipiscing turpis gravida ac. In congue, neque ac lobortis volutpat, libero mauris varius mi, vitae suscipit ipsum ligula vitae risus.</p>
    <span class="abs btn" style="left:147px;top:117px">Read More</span>
    <div class="abs divider"></div>
    <h4 class="abs" style="left:394px;top:18px">Contact Us</h4>
    <p class="abs" style="left:394px;top:42px">4720 Fenwick<br>Road,Glasgow, G12 7QX.<br>Phone: <span style="color:#fff">121 555 0148</span><br>Email: <span style="color:#fff">info@verdix-partners.com</span></p>
    <h4 class="abs" style="left:394px;top:114px">Connect Us</h4>
    <div class="abs social" style="left:486px;top:113px">
      <b style="background:#3b5ea8"></b><b style="background:#2aa3dd"></b><b style="background:#1f78b4"></b><b style="background:#3a3a3a"></b><b style="background:#f26a1b"></b>
    </div>
  </footer>
  <div class="abs base">Copyright © 2014. Verdix Partners. All Right Reserved</div>
</div>
</body>
</html>
```